New custom software business needs a Wordpress site

We need a Wordpress site for a new company based out of Chicago called 'Vellora Consulting'. Using a mix of on and off-shore resources we build custom software solutions, mainly focusing on small to medium sized companies. We help our customers "aspire" to do great things.
We have a basic site up here: https://brindlewave.example/. We worked on the content for it but not the branding. For now, this houses all the pages (except for a Contact Us page we'll be adding soon) for the foreseeable future.
We also have a new logo (attached) that we'd like to base the styling/colors on.
Target Market(s)
Small to medium sized companies that require tech resources
Industry/Entity Type
Software
Nice to have
- Teamwork, tech, professional but not elitist

```html
<!DOCTYPE html>
<html lang="en">
<head>
<meta charset="utf-8">
<title>Vellora Consulting</title>
<link href="https://fonts.googleapis.com/css2?family=Roboto:wght@300;400;500;700;900&display=swap" rel="stylesheet">
<style>
:root{
  --blue:#0b4fb0;
  --blue-dark:#063a86;
  --blue-deep:#0a2a63;
  --sky:#5cb8f0;
  --ink:#1d2433;
  --text:#3c4454;
  --muted:#7b8494;
  --pale:#e9f0fa;
  --white:#ffffff;
}
*{box-sizing:border-box;margin:0;padding:0}
html,body{width:1200px;height:4745px;overflow:hidden}
body{font-family:"Roboto",sans-serif;color:var(--text);background:var(--white)}
.page{position:relative;width:1200px;height:4745px;overflow:hidden}
.abs{position:absolute}
.btn{position:absolute;display:flex;align-items:center;justify-content:center;border-radius:22px;font-size:11px;font-weight:500;color:var(--white);background:var(--blue);box-shadow:0 6px 14px rgba(11,79,176,.25)}
.btn-dark{background:var(--ink)}
.heading{font-size:50px;font-weight:300;color:var(--ink);letter-spacing:-.5px}
.heading b{font-weight:700;color:var(--blue)}

/* hero */
.hero{position:absolute;left:0;top:0;width:1200px;height:630px;background:linear-gradient(100deg,#0d4fb5 0%,#1766c8 45%,#5c8fcf 100%)}
.hero-photo{position:absolute;left:420px;top:0;width:780px;height:630px;background:linear-gradient(135deg,rgba(40,110,200,.3),rgba(230,235,245,.55) 60%,rgba(40,100,190,.5))}
.hero-cut{position:absolute;left:0;top:0}
.brand{position:absolute;display:flex;align-items:center;gap:8px;color:var(--white);font-weight:700;font-size:20px;letter-spacing:1px}
.brand i{width:14px;height:14px;border-radius:50%;background:var(--white);display:block}
.nav{position:absolute;left:320px;top:34px;display:flex;gap:24px;font-size:12px;color:var(--white)}
.nav span:first-child{font-weight:700}
.help{position:absolute;left:928px;top:28px;display:flex;gap:10px;align-items:center;color:var(--white)}
.help .ic{width:30px;height:30px;border-radius:50%;background:var(--white);display:flex;align-items:center;justify-content:center}
.help small{display:block;font-size:9px;opacity:.9}
.help strong{font-size:13px;font-weight:400}
.hero-title{position:absolute;left:112px;top:220px;font-size:50px;color:var(--white);font-weight:300}
.hero-title b{font-weight:700}
.hero-text{position:absolute;left:112px;top:295px;width:330px;font-size:12px;line-height:18px;color:var(--white)}
.btn-hero{left:112px;top:387px;width:205px;height:41px;background:var(--sky);color:var(--blue-deep);font-size:10.5px;gap:6px}
.scroll{position:absolute;left:40px;top:590px;writing-mode:vertical-rl;transform:rotate(180deg);font-size:8px;letter-spacing:5px;color:var(--ink)}

/* about */
.ghost{position:absolute;left:0;width:1200px;text-align:center;top:690px;font-size:120px;font-weight:900;color:rgba(11,79,176,.05)}
.welcome{position:absolute;left:230px;top:785px;width:740px;text-align:center;font-size:17px;line-height:25px;color:var(--ink)}
.welcome .lead{font-size:26px;font-weight:700;color:var(--blue)}
.about-text{position:absolute;left:645px;top:977px;width:445px;font-size:11px;line-height:16.5px;color:var(--ink)}
.about-text p{margin-bottom:16px}

/* services */
.center{position:absolute;left:0;width:1200px;text-align:center}
.sub{font-size:12px;line-height:19px;color:var(--ink)}
.slide-card{position:absolute;left:300px;top:1644px;width:601px;height:498px;border-radius:4px;background:linear-gradient(180deg,#5e7fa6 0%,#264e86 55%,#0e2f66 100%);overflow:hidden}
.slide-card h3{position:absolute;left:66px;top:297px;font-size:21px;font-weight:400;color:var(--white)}
.slide-card p{position:absolute;left:66px;top:340px;width:460px;font-size:10.5px;line-height:16px;color:var(--white)}
.arrow{position:absolute;width:28px;height:26px;background:var(--blue);display:flex;align-items:center;justify-content:center}

/* why */
.cards{position:absolute;top:2492px;left:112px;display:flex;gap:49px}
.card{width:292px;height:263px;background:linear-gradient(180deg,#dce6f4,#f6f8fb);border-top:2px solid var(--blue);position:relative;box-shadow:0 6px 20px rgba(0,0,0,.06)}
.card .icon{position:absolute;left:32px;top:30px}
.card h4{position:absolute;left:32px;top:88px;width:190px;font-size:14.5px;font-weight:400;line-height:19px;color:var(--ink)}
.card .num{position:absolute;right:32px;top:95px;width:24px;height:24px;border-radius:50%;background:var(--white);font-size:8px;font-weight:700;color:var(--blue);display:flex;align-items:center;justify-content:center;box-shadow:0 2px 6px rgba(0,0,0,.08)}
.card p{position:absolute;left:32px;top:180px;width:230px;font-size:10.5px;line-height:16px;color:var(--muted)}

/* leadership */
.lead-title{position:absolute;left:112px;top:3148px;font-size:48px;font-weight:300;color:var(--ink)}
.lead-title b{font-weight:700;color:var(--blue)}
.dash{position:absolute;left:112px;top:3244px;width:26px;height:3px;background:var(--blue)}
.person{position:absolute;left:112px;top:3270px;font-size:16px;font-weight:700;color:var(--blue)}
.role{position:absolute;left:112px;top:3293px;font-size:9px;color:var(--ink)}
.lead-text{position:absolute;left:112px;top:3328px;width:405px;font-size:10.5px;line-height:16.5px;color:var(--ink)}
.lead-text p{margin-bottom:16px}

/* contact */
.cta{position:absolute;left:0;top:3960px;width:1200px;text-align:center;font-size:31px;font-weight:500;color:var(--white);line-height:38px}
.label{position:absolute;font-size:8.5px;color:var(--white);opacity:.85}
.field{position:absolute;height:32px;background:rgba(255,255,255,.28);border:1px solid rgba(255,255,255,.45);border-radius:2px}

/* footer */
.fcol h5{font-size:18px;font-weight:500;color:var(--white);position:relative;padding-top:10px}
.fcol h5:before{content:"";position:absolute;left:0;top:0;width:18px;height:2px;background:var(--white)}
.fcol ul{list-style:none;margin-top:22px}
.fcol li{font-size:11px;color:var(--white);margin-bottom:10px;display:flex;align-items:center;gap:8px}
.fcol li:before{content:"";width:7px;height:7px;border:1px solid var(--white);border-radius:50%}
.fcol.info li:before{display:none}
.social{display:flex;gap:8px;margin-top:14px}
.social i{width:30px;height:30px;border-radius:50%;background:rgba(255,255,255,.35);border:1px solid rgba(255,255,255,.6);display:block}
.copy{position:absolute;left:0;top:4706px;width:1200px;text-align:center;font-size:10px;color:var(--white);opacity:.85}
</style>
</head>
<body>
<div class="page">

  <!-- Hero -->
  <section class="hero">
    <div class="hero-photo" role="img" aria-label="Photo of two smiling colleagues working together on a laptop"></div>
    <svg class="hero-cut" width="1200" height="630" viewBox="0 0 1200 630"><polygon points="0,630 1200,630 1200,555 700,630" fill="#fff"/></svg>
    <div class="brand" style="left:112px;top:30px">VELLORA <i></i></div>
    <nav class="nav"><span>Home</span><span>About Us</span><span>Services</span><span>Why Vellora?</span><span>Vellora Leadership</span><span>Contact Us</span></nav>
    <div class="help">
      <div class="ic"><svg width="14" height="14" viewBox="0 0 24 24"><path d="M6.6 10.8a15 15 0 0 0 6.6 6.6l2.2-2.2c.3-.3.7-.4 1-.2 1.1.4 2.3.6 3.6.6.6 0 1 .4 1 1V20c0 .6-.4 1-1 1A17 17 0 0 1 3 4c0-.6.4-1 1-1h3.5c.6 0 1 .4 1 1 0 1.3.2 2.5.6 3.6.1.3 0 .7-.2 1z" fill="#0b4fb0"/></svg></div>
      <div><small>Need Help? Call Us:</small><strong>+1 555 014 2290</strong></div>
    </div>
    <h1 class="hero-title"><b>Vellora</b> Consulting</h1>
    <p class="hero-text">At Vellora, we are proud to have a team of seasoned IT professionals who understand what it takes to deliver a quality solution.</p>
    <div class="btn btn-hero"><svg width="10" height="10" viewBox="0 0 10 10"><rect x="1" y="2" width="8" height="7" fill="none" stroke="#0a2a63"/><line x1="1" y1="4" x2="9" y2="4" stroke="#0a2a63"/></svg>Schedule a Consultation</div>
  </section>
  <div class="scroll">SCROLL DOWN ⟶</div>

  <!-- About -->
  <div class="ghost">About Us</div>
  <p class="welcome"><span class="lead">Welcome to Vellora</span>, a software consulting company specializing in serving small to medium size businesses. We understand the <b>unique challenges and opportunities</b> that these companies face, and we are dedicated to helping them succeed through <b>innovative technology solutions.</b></p>
  <svg class="abs" style="left:110px;top:930px" width="425" height="410" viewBox="0 0 425 410">
    <defs><linearGradient id="tri" x1="0" y1="0" x2="1" y2="1"><stop offset="0" stop-color="#1f6bd0"/><stop offset="1" stop-color="#0b3f93"/></linearGradient></defs>
    <polygon points="209,0 425,368 0,368" fill="url(#tri)"/>
    <circle cx="215" cy="218" r="190" fill="#3a4a5e"/>
  </svg>
  <div class="abs" role="img" aria-label="Photo of two businessmen reviewing a document" style="left:135px;top:962px;width:380px;height:380px;border-radius:50%;background:radial-gradient(circle at 45% 40%,#8796aa,#2f3b4c 75%)"></div>
  <div class="about-text">
    <p>Our team of experienced professionals has a diverse range of skills and expertise, making us well-equipped to handle any project, big or small. We specialize in custom software development, working closely with our clients to understand their specific needs and build solutions that meet their requirements.</p>
    <p>From developing web and mobile applications to implementing cloud-based systems and integrating with existing platforms, we have the tools and knowledge to deliver results that drive success. We also offer a range of other services, including IT consulting, project management, and technical support, to help businesses optimize their operations and achieve their goals.</p>
    <p>At Vellora, we are committed to delivering high-quality results and exceptional customer service to our small to medium size business clients. We believe that clear communication and collaboration are key to the success of any project, and we work closely with our clients every step of the way to ensure their needs are met and expectations are exceeded.</p>
  </div>
  <div class="btn" style="left:645px;top:1285px;width:142px;height:42px">Read More</div>

  <!-- Services -->
  <h2 class="center heading" style="top:1472px"><b>Vellora</b> Consulting Services</h2>
  <p class="center sub" style="top:1548px">Vellora is a leading provider of economical custom software development and staff augmentation<br>services. We specialize in helping companies around the world access top talent...</p>
  <svg class="abs" style="left:0;top:1644px" width="1200" height="500" viewBox="0 0 1200 500">
    <defs>
      <linearGradient id="gl" x1="0" y1="0" x2="0" y2="1"><stop offset="0" stop-color="#c9ccd1"/><stop offset="1" stop-color="#9ea3aa"/></linearGradient>
    </defs>
    <polygon points="0,60 271,0 271,498 0,400" fill="url(#gl)" role="img" aria-label="Greyscale photo of hands holding people icons"/>
    <polygon points="929,0 1200,60 1200,400 929,498" fill="url(#gl)" role="img" aria-label="Greyscale photo of a team meeting"/>
  </svg>
  <div class="slide-card" role="img" aria-label="Photo of a presenter leading a meeting in a glass office">
    <h3>Custom Solution Delivery</h3>
    <p>Vellora offers a range of services focused on helping businesses and organizations deliver software solutions to their customers or users. This can include a wide variety of activities, such as designing and developing custom software...</p>
    <div class="btn" style="left:66px;top:414px;width:142px;height:42px">Read More</div>
  </div>
  <div class="arrow" style="left:203px;top:1874px"><svg width="8" height="10" viewBox="0 0 8 10"><path d="M6 1 2 5l4 4" stroke="#fff" stroke-width="1.5" fill="none"/></svg></div>
  <div class="arrow" style="left:966px;top:1874px"><svg width="8" height="10" viewBox="0 0 8 10"><path d="M2 1l4 4-4 4" stroke="#fff" stroke-width="1.5" fill="none"/></svg></div>

  <!-- Why -->
  <svg class="abs" style="left:0;top:2140px" width="1200" height="900" viewBox="0 0 1200 900">
    <defs>
      <linearGradient id="wbg" x1="0" y1="0" x2="0" y2="1"><stop offset="0" stop-color="#fff"/><stop offset=".5" stop-color="#e6edf7"/><stop offset="1" stop-color="#d7e3f3"/></linearGradient>
      <linearGradient id="wedge" x1="0" y1="0" x2="1" y2="0"><stop offset="0" stop-color="#1c5fc4"/><stop offset="1" stop-color="#0848a8"/></linearGradient>
    </defs>
    <rect width="1200" height="885" fill="url(#wbg)"/>
    <polygon points="0,885 1200,585 1200,760 370,855" fill="url(#wedge)"/>
    <polygon points="0,885 370,855 1200,760 1200,900 0,900" fill="#fff"/>
    <polygon points="0,860 0,885 370,855" fill="#d7e3f3"/>
  </svg>
  <h2 class="center heading" style="top:2276px">Why <b>Vellora</b> Consulting</h2>
  <p class="center sub" style="top:2350px">At Vellora, we are proud to have a team of seasoned IT professionals who understand what it takes to<br>deliver a quality solution. Our team members have a wealth of experience and expertise in a variety of<br>different areas, including software development, system integration, data migration, and software<br>maintenance and support.</p>
  <div class="cards">
    <div class="card">
      <svg class="icon" width="44" height="40" viewBox="0 0 44 40" fill="none" stroke="#1d2433" stroke-width="1.4"><circle cx="8" cy="8" r="4"/><circle cx="22" cy="8" r="4"/><circle cx="36" cy="8" r="4"/><path d="M2 36l6-22 6 22M16 36l6-22 6 22M30 36l6-22 6 22"/></svg>
      <h4>Differentiate from the competition</h4><span class="num">01</span>
      <p>Lorem ipsum dolor sit amet, consectetur adipiscing elit. Aliquam pellentesque sapien massa, vel pellentesque turpis.</p>
    </div>
    <div class="card">
      <svg class="icon" width="44" height="40" viewBox="0 0 44 40" fill="none" stroke="#1d2433" stroke-width="1.4"><circle cx="26" cy="14" r="10"/><circle cx="26" cy="14" r="5"/><circle cx="26" cy="14" r="1.5" fill="#0b4fb0"/><circle cx="10" cy="22" r="4"/><path d="M2 38c0-6 4-9 8-9s8 3 8 9"/></svg>
      <h4>Target the right people effectively</h4><span class="num">02</span>
      <p>Lorem ipsum dolor sit amet, consectetur adipiscing elit. Aliquam pellentesque sapien massa, vel pellentesque turpis.</p>
    </div>
    <div class="card">
      <svg class="icon" width="44" height="40" viewBox="0 0 44 40" fill="none" stroke="#1d2433" stroke-width="1.4"><rect x="2" y="2" width="16" height="12" rx="2"/><rect x="26" y="2" width="16" height="12" rx="2" stroke="#0b4fb0"/><circle cx="10" cy="24" r="4"/><circle cx="34" cy="24" r="4"/><path d="M2 38c0-5 3-8 8-8s8 3 8 8M26 38c0-5 3-8 8-8s8 3 8 8"/></svg>
      <h4>Communicate your story consistently</h4><span class="num">03</span>
      <p>Lorem ipsum dolor sit amet, consectetur adipiscing elit. Aliquam pellentesque sapien massa, vel pellentesque turpis.</p>
    </div>
  </div>
  <div class="btn btn-dark" style="left:529px;top:2838px;width:140px;height:42px">Read More</div>

  <!-- Leadership -->
  <h2 class="lead-title"><b>Vellora</b> Leadership</h2>
  <div class="dash"></div>
  <div class="person">Dean Harlow</div>
  <div class="role">Founder Of Vellora</div>
  <div class="lead-text">
    <p>As a leader, Dean is dedicated to fostering a culture of collaboration, innovation, and excellence within his team. He believes that by empowering his team members and encouraging open communication, he can create an environment that is conducive to creativity and problem-solving.</p>
    <p>Dean is a strong believer in the importance of continuous learning and development, and he is committed to providing his team with the resources and support they need to grow and succeed. He is also committed to building strong relationships with his team members, and he values their contributions and insights.</p>
  </div>
  <div class="btn" style="left:112px;top:3548px;width:142px;height:42px">Read More</div>
  <svg class="abs" style="left:571px;top:3115px" width="516" height="506" viewBox="0 0 516 506">
    <defs><linearGradient id="lt" x1="0" y1="0" x2="1" y2="1"><stop offset="0" stop-color="#1d66cc"/><stop offset="1" stop-color="#0a3e90"/></linearGradient></defs>
    <polygon points="258,110 516,506 0,506" fill="url(#lt)"/>
    <polygon points="258,260 392,470 124,470" fill="#fff"/>
  </svg>
  <div class="abs" role="img" aria-label="Photo of a smiling founder in a suit holding a tablet" style="left:688px;top:3118px;width:278px;height:500px;border-radius:120px 120px 0 0;background:linear-gradient(180deg,#c9a58a 0%,#b48c70 18%,#2a3f66 30%,#1c2e52 100%)"></div>

  <!-- Contact -->
  <svg class="abs" style="left:0;top:3740px" width="1200" height="1005" viewBox="0 0 1200 1005">
    <defs><linearGradient id="cb" x1="0" y1="0" x2="1" y2="1"><stop offset="0" stop-color="#0f3f8c"/><stop offset=".6" stop-color="#0a2d66"/><stop offset="1" stop-color="#061d45"/></linearGradient></defs>
    <polygon points="0,0 1200,120 1200,1005 0,1005" fill="#c8d7ec"/>
    <polygon points="0,180 1200,60 1200,1005 0,1005" fill="url(#cb)" role="img" aria-label="Dark blue tinted photo of a team collaborating"/>
  </svg>
  <h2 class="cta">Let's talk about how we can make<br>brands work for you</h2>
  <div class="label" style="left:214px;top:4074px">Name*</div>
  <div class="label" style="left:605px;top:4074px">Email*</div>
  <div class="field" style="left:214px;top:4092px;width:379px"></div>
  <div class="field" style="left:605px;top:4092px;width:379px"></div>
  <div class="label" style="left:214px;top:4139px">Company / Organization</div>
  <div class="label" style="left:605px;top:4139px">Job Title</div>
  <div class="field" style="left:214px;top:4158px;width:379px"></div>
  <div class="field" style="left:605px;top:4158px;width:379px"></div>
  <div class="label" style="left:214px;top:4208px">How can we help?*</div>
  <div class="field" style="left:214px;top:4226px;width:770px;height:84px"></div>
  <div class="btn" style="left:529px;top:4359px;width:140px;height:41px;background:#1360cc">Submit</div>

  <!-- Footer -->
  <svg class="abs" style="left:0;top:4450px" width="1200" height="260" viewBox="0 0 1200 260"><line x1="580" y1="0" x2="580" y2="240" stroke="rgba(255,255,255,.2)"/><line x1="853" y1="0" x2="853" y2="240" stroke="rgba(255,255,255,.2)"/><line x1="110" y1="245" x2="1090" y2="245" stroke="rgba(255,255,255,.2)"/></svg>
  <div class="brand" style="left:118px;top:4560px;font-size:22px">VELLORA <i></i></div>
  <div class="fcol abs" style="left:369px;top:4478px">
    <h5>Services</h5>
    <ul><li>Custom Solution Delivery</li><li>Staff Augmentation</li><li>Lorem ipsum dolor sit</li><li>Lorem ipsum dolor sit</li></ul>
  </div>
  <div class="fcol abs" style="left:658px;top:4478px">
    <h5>Quick Link</h5>
    <ul><li>About Us</li><li>Services</li><li>Why Vellora?</li><li>Vellora Leadership</li><li>Contact Us</li></ul>
  </div>
  <div class="fcol info abs" style="left:918px;top:4478px">
    <h5>Contact Info</h5>
    <ul><li>☏ +1 555 014 2290</li><li>✉ info@velloraconsulting.example</li></ul>
    <div class="social"><i></i><i></i><i></i><i></i></div>
  </div>
  <div class="copy">© 2022 Vellora Consulting. All Rights Reserved.</div>
</div>
</body>
</html>
```